Marketing Software Home Page Design
TELVARO
Marketing Software Home Page Design - Software
Creative Brief
Software
www.telvaro-demo.net
TELVARO is revolutionizing the way public relations professionals manage multimedia content for press releases and global campaigns. Our cloud based platform makes it easy to create a microsite that can display and distribute your video, photos, audio and documents to your media contacts in formats that can be that can be easily viewed and downloaded. TELVARO is mobile responsive, socially enabled and provides rich analytics. TELVARO is also the only global platform that can be translated in up to 10 languages with the click of a button.
One of the most critical features of TELVARO is the ability to learn how to use the platform in 30 minutes, giving you complete control of content distribution and the ability to make up to the minute changes. Our analytics also track WHO has downloaded the content along with on page metrics, social media tracking and embed video analytics.
How is TELVARO used?
-Multimedia News Release (MNR)
-Media Kits
-Product Launches
-Content Storage (video, photos, documents)
-Event Content Distribution
Clean, White space, modern
High Tech
Lime Green (see hex colors below)
Grey
White/ Black
left side
www.krate.example
www.fennelvault.example
quarnbymedia.example
Want a scrolling home page. Logo Colors: Reg: 141 Green: 198 Blue: 63 Hue: 60 Saturation: 138 Luminosity: 131 HEX CODE: #8DC63F (original) #88CC44 (websafe)

```html
<!DOCTYPE html>
<html lang="en">
<head>
<meta charset="utf-8">
<title>TELVARO – Simply. Communicate.</title>
<link href="https://fonts.googleapis.com/css2?family=Lato:ital,wght@0,400;0,700;0,900;1,400;1,700&display=swap" rel="stylesheet">
<style>
:root{
  --lime:#8DC63F;
  --lime-dark:#76ad2c;
  --ink:#333;
  --grey-text:#555;
  --grey-bg:#ebebeb;
  --line:#d6d6d6;
  --night:#2b2b2b;
  --white:#fff;
}
*{box-sizing:border-box;margin:0;padding:0}
html,body{width:1200px;height:2299px;overflow:hidden}
body{position:relative;font-family:'Lato',sans-serif;color:var(--ink);background:var(--white)}
.abs{position:absolute;white-space:nowrap}

/* header */
.topline{left:0;top:0;width:1200px;height:4px;background:var(--lime)}
.header{left:0;top:4px;width:1200px;height:118px;background:#f7f7f7;border-bottom:1px solid #ddd}
.brand{left:132px;top:18px;font-weight:900;font-size:54px;letter-spacing:-1px;color:var(--lime);line-height:1}
.tagline{left:137px;top:83px;font-size:17px;font-weight:700;color:#444;letter-spacing:.3px}
.social-btn{top:20px;height:22px;border:1px solid #ccc;background:#fff;font-size:11px;font-weight:700;color:#444;display:flex;align-items:center;justify-content:center;gap:4px;border-radius:2px}
.social-btn i{width:9px;height:9px;background:#999;display:block}
.nav-item{top:56px;height:38px;display:flex;align-items:center;font-size:12px;font-weight:700;color:#333}
.nav-item.on{background:var(--lime);color:#fff;justify-content:center}

/* hero */
.hero{left:0;top:122px;width:1200px;height:717px;background:linear-gradient(115deg,#6e7a80 0%,#59656b 40%,#4e5d63 70%,#3f4c52 100%)}
.hero-title{left:132px;top:232px;font-size:29px;font-weight:700;color:var(--lime)}
.hero-sub{left:133px;top:274px;font-size:19px;color:#fff;line-height:25px}
.btn{display:flex;align-items:center;justify-content:center;background:linear-gradient(#95cf48,#77b02c);color:#fff;font-size:18px;border:1px solid #6a9d26}
.devices{left:583px;top:157px;width:485px;height:338px;background:linear-gradient(135deg,#2a7fb8,#1d5c8a);border-radius:10px}
.portrait{left:141px;top:503px;width:122px;height:122px;border-radius:50%;border:5px solid #e8e8e8;background:radial-gradient(circle,#b98a6e,#5a3a2c)}
.quote{left:276px;top:527px;width:790px;font-size:15px;font-style:italic;color:#fff;line-height:28px;white-space:normal}
.quote b{color:#9aa3a7;font-size:30px;font-style:normal;vertical-align:-8px}
.cite{left:700px;top:612px;width:353px;text-align:right;font-size:15px;font-style:italic;font-weight:700;color:var(--lime)}
.brand-strip{left:132px;top:668px;width:937px;height:98px;background:rgba(255,255,255,.22);display:flex;align-items:center;justify-content:space-around}
.brand-strip span{font-size:28px;font-weight:900;color:#1f4f9c}

/* features */
.features{left:0;top:839px;width:1200px;height:293px;background:var(--grey-bg)}
.feat-title{left:133px;top:839px;height:45px;padding:0 18px;background:var(--lime);color:#fff;font-size:21px;font-weight:700;display:flex;align-items:center;justify-content:center}
.feat-list{left:135px;top:908px;width:600px;list-style:none;white-space:normal}
.feat-list li{position:relative;padding-left:23px;font-size:17px;color:var(--grey-text);line-height:22.5px;margin-bottom:21px}
.feat-list li::before{content:"";position:absolute;left:0;top:4px;width:9px;height:13px;border:2.5px solid var(--lime);border-radius:3px}
.contact-box{left:775px;top:864px;width:294px;height:267px;background:#f9f9f9;border:1px solid var(--line)}
.contact-title{left:0;top:12px;width:100%;text-align:center;font-size:22px;color:var(--lime)}
.field{left:27px;width:239px;height:24px;background:#fff;border:1px solid #ccc;font-size:12px;font-style:italic;color:#666;padding:4px 6px}
.submit{left:113px;top:219px;width:68px;height:27px;background:#222;color:#fff;font-size:15px;font-weight:700;display:flex;align-items:center;justify-content:center;border-radius:2px}

/* how used */
.how-title{left:0;top:1164px;width:1200px;text-align:center;font-size:34px;font-weight:700;color:var(--lime)}
.use{top:1236px;width:160px;text-align:center}
.use svg{display:block;margin:0 auto}
.use p{margin-top:10px;font-size:15px;font-weight:700;color:#555;line-height:20px}

/* problem */
.problem{left:0;top:1451px;width:1200px;height:518px;background:linear-gradient(110deg,#1f3a5a 0%,#2d4a6c 45%,#1c3553 100%)}
.problem-title{left:0;top:1485px;width:1200px;text-align:center;font-size:34px;font-weight:700;color:#fff}
.stat-num{left:132px;width:76px;height:76px;border-radius:50%;background:#fff;border:4px solid #ddd;display:flex;align-items:center;justify-content:center;font-size:21px;font-weight:700;color:#222}
.stat-text{left:222px;width:300px;font-size:15px;font-weight:700;color:#fff;line-height:21px;white-space:normal}
.video{left:625px;top:1557px;width:444px;height:250px;background:linear-gradient(#e6e6e6,#cfcfcf)}
.controls{left:625px;top:1807px;width:444px;height:47px;background:#1a1a1a}

/* as seen in */
.seen-title{left:0;top:2004px;width:1200px;text-align:center;font-size:28px;color:#444}
.seen-box{left:151px;top:2055px;width:900px;height:112px;border:1px solid var(--line);display:flex;align-items:center;justify-content:space-around}
.seen-box span{font-size:24px;font-weight:900;color:#222}

/* footer */
.foot-nav{left:0;top:2205px;width:1200px;height:47px;background:var(--night);display:flex;align-items:center;justify-content:center;gap:20px;font-size:14px;color:#fff}
.foot-nav em{font-style:normal;color:#ccc}
.foot-bar{left:0;top:2252px;width:1200px;height:47px;background:var(--lime)}
.copy{left:138px;top:2267px;font-size:12px;color:#333}
</style>
</head>
<body>

<div class="abs topline"></div>
<header class="abs header"></header>
<div class="abs brand">TELVARO</div>
<div class="abs tagline">Simply. Communicate.</div>

<div class="abs social-btn" style="left:845px;width:65px"><i></i>Chirper</div>
<div class="abs social-btn" style="left:931px;width:68px"><i></i>ProLink</div>
<div class="abs social-btn" style="left:1017px;width:52px"><i></i>Favor</div>

<nav>
  <div class="abs nav-item on" style="left:444px;width:71px">HOME</div>
  <div class="abs nav-item" style="left:527px">PRODUCTS AND FEATURES</div>
  <div class="abs nav-item" style="left:706px">TELVARO FOR...</div>
  <div class="abs nav-item" style="left:813px">ABOUT US</div>
  <div class="abs nav-item on" style="left:902px;width:87px">CONTACT</div>
  <div class="abs nav-item on" style="left:999px;width:71px">LOGIN</div>
</nav>

<section class="abs hero" role="img" aria-label="Blurred photo of people working at laptops, tinted grey"></section>
<h1 class="abs hero-title">Simply. Communicate.</h1>
<p class="abs hero-sub">The Leading Multimedia News Release Platform<br>for Communications Professionals</p>
<div class="abs btn" style="left:132px;top:350px;width:133px;height:34px">Read More</div>
<div class="abs devices" role="img" aria-label="Desktop monitor, tablet and phone showing a branded multimedia news release page"></div>

<div class="abs portrait" role="img" aria-label="Portrait photo of the quoted client"></div>
<p class="abs quote"><b>“</b> I’ve worked with TELVARO several times and they are a fraction of the cost of other Multimedia News Release Solutions. It was perfect to both distribute campaign press releases as well as make it easy to get our multimedia content in to the hands of reporters. The experience has been great! <b>”</b></p>
<p class="abs cite">-Marissa Delvane, SVP, Halloway Crane</p>

<div class="abs brand-strip">
  <span>Calvexa</span><span>Norbrin</span><span>Tallywave</span><span>Quenford</span><span>Brisolm</span>
</div>

<section class="abs features"></section>
<div class="abs feat-title">TELVARO MAKES IT SIMPLE TO</div>
<ul class="abs feat-list">
  <li>Leverage Your Multimedia Content To Increase Earned Media Coverage</li>
  <li>Create A Branded Web Page So Journalists Can View Your Story And Quickly Download Your Video, Photos And Documents.</li>
  <li>Collect Deep Analytics Including Who Downloads Your Content And Where It’s Located.</li>
  <li>Manage, Store And Share Your Multimedia Content</li>
</ul>

<form class="abs contact-box">
  <div class="abs contact-title">CONTACT US</div>
  <div class="abs field" style="top:45px">Name</div>
  <div class="abs field" style="top:79px">Email</div>
  <div class="abs field" style="top:113px">Phone</div>
  <div class="abs field" style="top:148px;height:61px">Message</div>
  <div class="abs submit">Submit</div>
</form>

<h2 class="abs how-title">How is TELVARO Used?</h2>

<div class="abs use" style="left:137px">
  <svg width="120" height="120" viewBox="0 0 120 120"><circle cx="60" cy="64" r="55" fill="#ccc"/><circle cx="60" cy="58" r="55" fill="#fff" stroke="#8DC63F" stroke-width="6"/>
  <rect x="32" y="38" width="56" height="40" rx="6" fill="none" stroke="#555" stroke-width="6"/><rect x="42" y="47" width="12" height="10" fill="#555"/><rect x="58" y="47" width="22" height="4" fill="#555"/><rect x="58" y="55" width="22" height="4" fill="#555"/><rect x="42" y="63" width="38" height="4" fill="#555"/></svg>
  <p>Multimedia News<br>Release (MNR)</p>
</div>
<div class="abs use" style="left:329px">
  <svg width="120" height="120" viewBox="0 0 120 120"><circle cx="60" cy="64" r="55" fill="#ccc"/><circle cx="60" cy="58" r="55" fill="#fff" stroke="#8DC63F" stroke-width="6"/>
  <rect x="28" y="36" width="56" height="38" rx="3" fill="none" stroke="#555" stroke-width="5"/><rect x="46" y="76" width="20" height="6" fill="#555"/><rect x="34" y="42" width="18" height="8" fill="#555"/><rect x="56" y="44" width="22" height="3" fill="#555"/><rect x="56" y="52" width="22" height="3" fill="#555"/><rect x="74" y="60" width="16" height="22" rx="8" fill="#555"/></svg>
  <p>Media<br>Rooms</p>
</div>
<div class="abs use" style="left:521px">
  <svg width="120" height="120" viewBox="0 0 120 120"><circle cx="60" cy="64" r="55" fill="#ccc"/><circle cx="60" cy="58" r="55" fill="#fff" stroke="#8DC63F" stroke-width="6"/>
  <path d="M60 32 C68 42 68 60 66 74 H54 C52 60 52 42 60 32Z" fill="#555"/><path d="M54 64 L46 78 L54 76Z M66 64 L74 78 L66 76Z" fill="#555"/><rect x="57" y="78" width="6" height="8" fill="#555"/></svg>
  <p>Product<br>Launches</p>
</div>
<div class="abs use" style="left:712px">
  <svg width="120" height="120" viewBox="0 0 120 120"><circle cx="60" cy="64" r="55" fill="#ccc"/><circle cx="60" cy="58" r="55" fill="#fff" stroke="#8DC63F" stroke-width="6"/>
  <rect x="48" y="36" width="22" height="16" fill="#555"/><rect x="38" y="52" width="44" height="30" rx="4" fill="#555"/><rect x="38" y="56" width="44" height="3" fill="#fff"/></svg>
  <p>Content<br>Storage</p>
</div>
<div class="abs use" style="left:904px">
  <svg width="120" height="120" viewBox="0 0 120 120"><circle cx="60" cy="64" r="55" fill="#ccc"/><circle cx="60" cy="58" r="55" fill="#fff" stroke="#8DC63F" stroke-width="6"/>
  <path d="M38 54 L60 36 L82 54 V80 H38Z" fill="none" stroke="#555" stroke-width="4"/><path d="M60 44 L72 58 H65 V70 H55 V58 H48Z" fill="#555"/></svg>
  <p>Event Content<br>Distribution</p>
</div>

<section class="abs problem" role="img" aria-label="Dark blue tinted city and world map collage"></section>
<h2 class="abs problem-title">What’s the Problem?</h2>

<div class="abs stat-num" style="top:1565px">75%</div>
<p class="abs stat-text" style="top:1583px">75% of journalists include photos, videos or infographics in their stories.</p>
<div class="abs stat-num" style="top:1659px">94%</div>
<p class="abs stat-text" style="top:1680px">Views increase by 94% when multimedia content is included in your article.</p>
<div class="abs stat-num" style="top:1753px">100%</div>
<p class="abs stat-text" style="top:1771px">100% of public relations professionals find managing these large files... frustrating!</p>

<div class="abs video" role="img" aria-label="Explainer video frame with sketched cartoon characters and the headline about feeling your pain"></div>
<svg class="abs" style="left:804px;top:1647px" width="86" height="58" viewBox="0 0 86 58"><rect width="86" height="58" rx="8" fill="rgba(40,40,40,.8)"/><path d="M36 18 L54 29 L36 40Z" fill="#fff"/></svg>
<div class="abs controls"></div>
<svg class="abs" style="left:625px;top:1807px" width="444" height="47" viewBox="0 0 444 47">
  <rect x="28" y="21" width="258" height="6" rx="3" fill="#444"/><rect x="28" y="21" width="187" height="6" rx="3" fill="#e02020"/><circle cx="203" cy="24" r="7" fill="#eee"/>
  <rect x="318" y="16" width="16" height="2" fill="#888"/><rect x="318" y="21" width="16" height="2" fill="#888"/><rect x="318" y="26" width="16" height="2" fill="#888"/>
  <rect x="353" y="15" width="40" height="17" rx="8" fill="#333"/><text x="373" y="27" fill="#ddd" font-size="9" font-family="Lato,sans-serif" text-anchor="middle">HD ON</text>
  <circle cx="412" cy="24" r="11" fill="#ddd"/></svg>

<div class="abs btn" style="left:252px;top:1896px;width:125px;height:34px">Case Studies</div>
<div class="abs btn" style="left:777px;top:1896px;width:124px;height:34px">Contact Us</div>

<h2 class="abs seen-title" style="font-weight:400">As Seen In</h2>
<div class="abs seen-box">
  <span>Oakridge Ledger</span><span>PR Bulletin</span><span>Comms Daily</span><span>capitalvoice</span>
</div>

<nav class="abs foot-nav">
  <span>Home</span><em>|</em><span>Products and Features</span><em>|</em><span>TELVARO for...</span><em>|</em><span>About Us</span><em>|</em><span>Contact</span>
</nav>
<footer class="abs foot-bar"></footer>
<div class="abs copy">© 2015 TELVARO All Rights Reserved</div>
<svg class="abs" style="left:915px;top:2260px" width="156" height="32" viewBox="0 0 156 32">
  <circle cx="17" cy="16" r="14" fill="none" stroke="#fff" stroke-width="2"/>
  <circle cx="57" cy="16" r="14" fill="none" stroke="#fff" stroke-width="2"/>
  <circle cx="98" cy="16" r="14" fill="none" stroke="#fff" stroke-width="2"/>
  <circle cx="139" cy="16" r="14" fill="none" stroke="#fff" stroke-width="2"/>
</svg>

</body>
</html>
```